Trucking company needs business card design

New trucking company needs fresh ideas on a business card. Contracted exclusively to Parcelwing, can incorporate their colors or style, but not necessary.
Beckley Haulage, Inc (with or without the Inc.)
Dale Quimby, CEO
208-555-0174
PO BOX 672
Orrin Falls, NV

Need to add my email address to the card--beckleyhaulageinc@quillpost.net

Trucking Company

```html
<!DOCTYPE html>
<html lang="en">
<head>
<meta charset="utf-8">
<title>Beckley Haulage – Business Card</title>
<link href="https://fonts.googleapis.com/css2?family=Ubuntu:wght@400;500;700&display=swap" rel="stylesheet">
<style>
  :root {
    --backdrop: #3a403c;
    --card: #ffffff;
    --brand-blue: #2a1ff2;
    --ink: #111111;
  }
  * { margin: 0; padding: 0; box-sizing: border-box; }
  html, body {
    width: 1200px;
    height: 1000px;
    overflow: hidden;
    background: var(--backdrop);
    font-family: "Ubuntu", sans-serif;
  }
  .business-card {
    position: absolute;
    left: 180px;
    top: 260px;
    width: 840px;
    height: 480px;
    background: var(--card);
  }
  .brand-name {
    position: absolute;
    left: 330px;
    top: 110px;
    width: 480px;
    color: var(--brand-blue);
    font-weight: 700;
    font-size: 76px;
    line-height: 0.9;
    letter-spacing: -1px;
    text-transform: uppercase;
    text-align: left;
  }
  .brand-name span { display: block; }
  .contact-block {
    position: absolute;
    left: 170px;
    top: 290px;
    width: 340px;
    text-align: center;
    color: var(--ink);
    line-height: 1.2;
  }
  .contact-name {
    font-weight: 700;
    font-size: 24px;
  }
  .contact-phone {
    font-weight: 700;
    font-size: 17px;
  }
  .contact-address {
    font-weight: 400;
    font-size: 17px;
  }
  .contact-email {
    font-weight: 400;
    font-size: 16px;
    margin-top: 4px;
  }
</style>
</head>
<body>
  <section class="business-card">
    <h1 class="brand-name"><span>Beckley</span><span>Haulage</span></h1>
    <div class="contact-block">
      <p class="contact-name">Dale Quimby, CEO</p>
      <p class="contact-phone">208-555-0174</p>
      <p class="contact-address">PO BOX 672</p>
      <p class="contact-address">Orrin Falls, NV</p>
      <p class="contact-email">beckleyhaulageinc@quillpost.net</p>
    </div>
  </section>
</body>
</html>
```